This book will apply the 12 Steps to gaming addiction, also known as video game addiction. The primary purpose of the book is to provide an effective solution for this new type of addiction. The solution is based on the rich and successful concepts of traditional twelve-step programs like RL.

The title on the cover will be "Nine Doors Past the Glowing Screen" and "by Martin Quorby". A subtitle can be used if it works in your design of "A Practical Path Beyond Compulsive Console Play". Cover will be for a 6" x 9" book approximately 110 pages in length.

Some back cover text including some review quotes and an author bio are in the attached Word doc. There is also an author photo attached for for the back cover.

Requirements
Must have
• For the cover design it could be stylized, or an image, a partial image, or whatever. I am open to suggestions. Think about what would be noticed by a person searching for help with moderating their video game use, or by the parents or loved ones of problem gamers. Something contemporary and eye catching.

```html
<!DOCTYPE html>
<html lang="en">
<head>
<meta charset="utf-8">
<title>Nine Doors Past the Glowing Screen – Cover Wrap</title>
<link rel="stylesheet" href="https://fonts.googleapis.com/css2?family=Oswald:wght@400;500;600&family=Open+Sans:ital,wght@0,400;0,600;1,400&display=swap">
<style>
  :root {
    --navy: #14244a;
    --yellow: #d8c41e;
    --ink: #3a3a3a;
    --white: #ffffff;
    --canvas: #ececec;
    --body-on-navy: #eef0f5;
  }
  * { box-sizing: border-box; margin: 0; padding: 0; }
  html, body { width: 804px; height: 1200px; overflow: hidden; }
  body { background: var(--canvas); position: relative; font-family: "Open Sans", sans-serif; }

  .cover-wrap {
    position: absolute; left: 12px; top: 324px;
    width: 780px; height: 552px;
    display: flex;
    box-shadow: 0 6px 18px rgba(0,0,0,.28);
  }

  /* Back cover */
  .back-cover {
    width: 368px; height: 100%;
    background: var(--navy);
    color: var(--body-on-navy);
    padding: 20px 18px 0 28px;
    position: relative;
  }
  .praise-heading {
    font-family: "Oswald", sans-serif; font-weight: 500;
    font-size: 12.5px; letter-spacing: .1px; color: var(--white);
    white-space: nowrap; margin-bottom: 8px;
  }
  .praise-heading .accent { color: var(--yellow); }
  .quote { position: relative; padding-left: 11px; margin-bottom: 9px; }
  .quote::before {
    content: "\201C"; position: absolute; left: 0; top: -3px;
    font-family: "Oswald", sans-serif; font-size: 14px; color: var(--yellow); font-weight: 600;
  }
  .quote-text { font-size: 7.4px; line-height: 1.42; }
  .quote-text .close { font-family: "Oswald", sans-serif; color: var(--yellow); font-size: 10px; font-weight: 600; line-height: 0; }
  .quote-source { font-size: 7.2px; color: var(--yellow); margin-top: 2px; }
  .section-break {
    display: flex; align-items: center; gap: 4px;
    margin: 12px 0 11px 10px;
    font-family: "Oswald", sans-serif; font-weight: 500;
    font-size: 13px; color: var(--yellow); white-space: nowrap;
  }
  .section-break::before, .section-break::after {
    content: ""; flex: 1; height: 1px; background: var(--white);
  }
  .blurb { padding-left: 10px; }
  .blurb p { font-size: 7.4px; line-height: 1.42; margin-bottom: 9px; }
  .about-author { position: absolute; left: 38px; right: 18px; top: 440px; display: flex; gap: 9px; }
  .author-photo {
    width: 73px; height: 78px; flex: none;
    border: 2px solid var(--white);
    background: linear-gradient(160deg, #6f8f5a, #3c4a3c 55%, #1e2a3e);
  }
  .author-bio { flex: 1; }
  .about-heading {
    display: flex; align-items: center; gap: 6px;
    font-weight: 600; font-style: italic; font-size: 9.5px; color: var(--yellow); margin-bottom: 5px;
  }
  .about-heading::after { content: ""; flex: 1; height: 1px; background: var(--yellow); }
  .author-bio p { font-size: 6.9px; font-style: italic; line-height: 1.5; }

  /* Spine */
  .spine { width: 45px; height: 100%; display: flex; flex-direction: column; }
  .spine-title {
    flex: 1; background: var(--navy);
    writing-mode: vertical-rl;
    display: flex; align-items: center; justify-content: flex-start;
    padding-top: 22px;
    font-family: "Oswald", sans-serif; white-space: nowrap;
  }
  .spine-title .lead { color: var(--yellow); font-size: 19px; font-weight: 600; letter-spacing: .3px; }
  .spine-title .rest { color: var(--white); font-size: 13px; font-weight: 500; margin-top: 8px; letter-spacing: .4px; }
  .spine-author {
    height: 143px; background: var(--yellow);
    writing-mode: vertical-rl;
    display: flex; align-items: center; justify-content: center;
    font-family: "Oswald", sans-serif; font-weight: 600; font-size: 16px; color: var(--navy);
  }

  /* Front cover */
  .front-cover { width: 367px; height: 100%; background: var(--white); position: relative; }
  .front-title { position: absolute; top: 44px; left: 0; right: 0; text-align: center; font-family: "Oswald", sans-serif; }
  .front-title .line-one { display: block; font-size: 39px; font-weight: 500; color: var(--yellow); line-height: 1.05; }
  .front-title .line-two { display: block; font-size: 26px; font-weight: 500; color: var(--ink); line-height: 1.15; }
  .subtitle-pill {
    position: absolute; top: 118px; left: 50%; transform: translateX(-50%);
    border: 1px solid var(--ink); border-radius: 10px;
    padding: 1px 9px; white-space: nowrap;
    font-size: 9.4px; color: var(--ink);
  }
  .cover-photo {
    position: absolute; top: 142px; left: 0; right: 0; height: 320px;
    background:
      linear-gradient(to bottom, rgba(255,255,255,0) 80%, #fff 100%),
      linear-gradient(to bottom, #f4f4f2 0%, #ecebe6 38%, #e6d531 52%, #d9c81e 68%, #cfcfcb 80%, #efefec 100%);
  }
  .front-author {
    position: absolute; bottom: 20px; left: 0; right: 0; text-align: center;
    font-family: "Oswald", sans-serif; font-weight: 500; font-size: 25px; color: #222; letter-spacing: .5px;
  }
</style>
</head>
<body>
  <main class="cover-wrap">
    <section class="back-cover">
      <h2 class="praise-heading"><span class="accent">PRAISE FOR NINE DOORS PAST</span> THE GLOWING SCREEN</h2>

      <div class="quote">
        <p class="quote-text">A must-read for anyone who is addicted to or thinks they may have a problem with digital gaming. This eloquent work will also be useful to academics and clinicians exploring potential solutions. The author recognizes the similarities between gaming addiction and other addictions, and logically applies one of the most effective known solutions for addiction - The Twelve Steps</p>
        <p class="quote-source">Dale Pennwick, Noted Interventionist and Keynote Speaker</p>
      </div>

      <div class="quote">
        <p class="quote-text">If you suffer from digital gaming addiction, I strongly encourage you to use this book as your road map to get you back to the real world. <span class="close">&#8221;</span></p>
        <p class="quote-source">Owen Trasker, Founder of Feedline Weekly.</p>
      </div>

      <div class="quote">
        <p class="quote-text">As a high school teacher for 24 years, husband, father, coach, and 12-Step member, I can assure you that this book will transform the life of anyone who is addicted to video games. Well written, easy to understand, and a wonderful book that will provide you with a clear road map to recovery, and this includes teenagers, a group I have been working with in the classroom for decades. <span class="close">&#8221;</span></p>
        <p class="quote-source">Rafael Montero, Harbor Vale High School Teacher.</p>
      </div>

      <h3 class="section-break">OR SOME OTHER BREAK TO SEPARATE SECTIONS</h3>

      <div class="blurb">
        <p>An effective solution to the challenge of Digital Gaming Addiction (aka Video Game Addiction) based on the rich and successful tradition of the Twelve Steps.</p>
        <p>Addiction to Digital Gaming is a new and troubling phenomenon that has burst upon an unprepared society with alarming speed. Many people crave the use of Digital Games in a strikingly similar way to any other addict. Digital Games are a complex software and hardware system that have been designed to promote continued and progressive usage. This sophisticated technology clearly feeds on natural addictive tendencies.</p>
        <p>The 12 Steps are one of the most effective methods for treating addiction in human history. Originating with Recovery League in 1939, the 12 Steps have since been used to treat a variety of other addictions, including drugs, sex, gambling, eating disorders, and many others. Now in this groundbreaking work the 12 Steps are applied to the complex and evolving contemporary phenomenon of Digital Gaming Addiction.</p>
      </div>

      <div class="about-author">
        <div class="author-photo" role="img" aria-label="Author portrait photograph"></div>
        <div class="author-bio">
          <h4 class="about-heading">About the Author</h4>
          <p>Marty Quorby is a Technology Consultant and Writer with many years of professional coding and consulting experience. He also struggled with addiction to drugs and alcohol and is now clean and sober in a Twelve-Step program for over 17 years. This unique combination of 12-Step experience and technology expertise led him to create Nine Doors Past the Glowing Screen.</p>
        </div>
      </div>
    </section>

    <section class="spine">
      <div class="spine-title"><span class="lead">NINE DOORS PAST</span><span class="rest">THE GLOWING SCREEN</span></div>
      <div class="spine-author">MARTIN QUORBY</div>
    </section>

    <section class="front-cover">
      <h1 class="front-title">
        <span class="line-one">NINE DOORS PAST</span>
        <span class="line-two">THE GLOWING SCREEN</span>
      </h1>
      <p class="subtitle-pill">A Practical Path Beyond Compulsive Console Play</p>
      <div class="cover-photo" role="img" aria-label="Photograph of a young woman reaching to take a game controller from a man playing video games on a yellow sofa in a bright white room"></div>
      <p class="front-author">MARTIN QUORBY</p>
    </section>
  </main>
</body>
</html>
```